Business card design needed

We are a wine business involved in winemaking, broking and packaging on behalf of clients globally with the majority being Asian. The design should be quite traditional and classic with some red used, font used should be easily read.

Target Market(s)

Trade customers other business owners

Industry/Entity Type

Business

Contact Information for Business Card

Rosalind Thwaite
Meridale Wine Collective
PO Box 738, Fenwick Vale
South Australia 5187
Phone: +61 (0)455 982 317
Email: kvcellars@brightmail.example

Logo styles of interest
Lettermark Logo

```html
<!DOCTYPE html>
<html lang="en">
<head>
<meta charset="utf-8">
<title>Rosalind Thwaite — Business Card</title>
<link rel="stylesheet" href="https://fonts.googleapis.com/css2?family=Poiret+One&display=swap">
<style>
  :root {
    --wine-red: #620000;
    --paper-white: #ffffff;
    --card-width: 741px;
    --card-height: 1200px;
    --text-right: 49px;
  }
  html, body {
    margin: 0;
    padding: 0;
    width: var(--card-width);
    height: var(--card-height);
    overflow: hidden;
    background: var(--wine-red);
  }
  .business-card {
    position: relative;
    width: var(--card-width);
    height: var(--card-height);
    background: var(--wine-red);
    color: var(--paper-white);
    font-family: "Poiret One", sans-serif;
    overflow: hidden;
  }
  .bottle-glass-art {
    position: absolute;
    left: 0;
    top: 0;
    width: 256px;
    height: var(--card-height);
  }
  .art-band {
    position: absolute;
    left: 0;
    background: var(--paper-white);
  }
  .art-neck { top: 89px;  height: 296px; width: 73px; }
  .art-body { top: 385px; height: 240px; width: 162px; }
  .art-bowl { top: 625px; height: 340px; width: 256px; }
  .art-base { top: 965px; height: 235px; width: 162px; }
  .text-line {
    position: absolute;
    right: var(--text-right);
    margin: 0;
    white-space: nowrap;
    text-align: right;
    line-height: 1;
    font-weight: 400;
  }
  .holder-name {
    top: 140px;
    font-size: 52px;
    letter-spacing: 4.5px;
  }
  .business-line {
    top: 201px;
    font-size: 33px;
    letter-spacing: 3px;
  }
  .postal-line {
    top: 996px;
    font-size: 29px;
    letter-spacing: 2px;
  }
  .region-line {
    top: 1036px;
    font-size: 29px;
    letter-spacing: 2px;
  }
  .phone-line {
    top: 1085px;
    font-size: 23px;
    letter-spacing: 1.6px;
  }
  .email-line {
    top: 1122px;
    font-size: 23px;
    letter-spacing: 1.6px;
  }
</style>
</head>
<body>
  <main class="business-card">
    <div class="bottle-glass-art" role="img" aria-label="White silhouette of a wine bottle and wine glass along the left edge">
      <div class="art-band art-neck"></div>
      <div class="art-band art-body"></div>
      <div class="art-band art-bowl"></div>
      <div class="art-band art-base"></div>
    </div>

    <h1 class="text-line holder-name">Rosalind Thwaite</h1>
    <p class="text-line business-line">Meridale Wine</p>

    <p class="text-line postal-line">Collective PO Box 738</p>
    <p class="text-line region-line">Fenwick Vale South Australia 5187</p>
    <p class="text-line phone-line">Phone: +61 (0)455 982 317</p>
    <p class="text-line email-line">Email: kvcellars@brightmail.example</p>
  </main>
</body>
</html>
```